Exciting & Elegant Stationary Pack

Stationary consists of
1. Letter head / Envelope
2. Business Card
3. Invoice
4. 40x40mm sticker

Attached files;

1. Logo (Other formats available on request)
2. MS word Doc - For information and description of design
3. Website image (This will be our new website so use the colours so everything ties together)
4. Sample of stationary pack we like, but feel free to be creative

Target Market(s)

Home improvement

Industry/Entity Type

Construction

Other font styles liked:
• Leave up to designer - We like font used on (website attached image)

Requirements
Must have
• Please look at uploaded file of sample website and use colours
Nice to have
• Any type of business card design - eg. metal, die cut, embossed, etc...

```html
<!DOCTYPE html>
<html lang="en">
<head>
<meta charset="utf-8">
<title>Grout &amp; Level – Business Cards</title>
<link rel="stylesheet" href="https://fonts.googleapis.com/css2?family=Montserrat:wght@400;500;700;800&display=swap">
<style>
  :root {
    --sky: #9dc3e4;
    --navy: #17466f;
    --ink: #1d3f66;
    --red: #d8262f;
    --white: #ffffff;
    --band-dark: #161616;
    --band-light: #e9e9e9;
    --band-blue: #2f6ea6;
  }
  * { box-sizing: border-box; margin: 0; padding: 0; }
  html, body { width: 1200px; height: 2571px; overflow: hidden; }
  body { font-family: "Montserrat", sans-serif; background: var(--band-light); }

  .band { position: relative; width: 1200px; height: 857px; overflow: hidden; }
  .band--dark { background: var(--band-dark); }
  .band--light { background: var(--band-light); }
  .band--blue { background: var(--band-blue); }

  .card { position: absolute; overflow: hidden; background: var(--sky); box-shadow: 0 12px 30px rgba(0,0,0,.35); }
  .card svg.card-art { position: absolute; inset: 0; width: 100%; height: 100%; }
  .card--landscape { width: 540px; height: 330px; }
  .card--portrait { width: 330px; height: 540px; }
  .card--wide { width: 620px; height: 378px; }

  .wordmark { position: absolute; color: var(--white); font-weight: 800; letter-spacing: 1px; line-height: 1; white-space: nowrap; }

  /* front, landscape */
  .front-landscape { left: 40px; top: 263px; }
  .front-landscape .wordmark { right: 32px; top: 110px; font-size: 40px; }

  /* front, portrait */
  .front-portrait { left: 210px; top: 158px; }
  .front-portrait .wordmark { left: 165px; top: 270px; font-size: 40px; transform: translate(-50%, -50%) rotate(-90deg); }

  /* back, portrait */
  .back-upright { left: 630px; top: 158px; }
  .back-turned { left: 725px; top: 158px; transform: rotate(-90deg); }
  .back .identity { position: absolute; left: 0; right: 0; top: 38px; text-align: center; }
  .back .company { color: var(--ink); font-weight: 800; font-size: 17px; letter-spacing: .5px; }
  .back .licence { color: var(--red); font-weight: 700; font-size: 12px; margin-top: 3px; }
  .back .person { color: var(--ink); font-weight: 700; font-size: 20px; margin-top: 22px; }
  .back .role { color: var(--red); font-weight: 500; font-size: 13px; margin-top: 2px; }
  .back .contacts { position: absolute; left: 0; right: 0; top: 225px; list-style: none; text-align: center; }
  .back .contacts li { height: 100px; color: var(--white); font-weight: 700; font-size: 13px; white-space: nowrap; }
  .back .contacts svg { display: block; margin: 0 auto 12px; width: 34px; height: 34px; }

  /* address card */
  .address-card { left: 290px; top: 240px; }
  .address-card .details { position: absolute; left: 120px; top: 48px; color: var(--white); font-size: 19px; line-height: 1.3; font-weight: 500; }
  .address-card .company { color: var(--ink); font-weight: 800; font-size: 21px; letter-spacing: .5px; }
  .address-card .label { color: var(--red); font-weight: 700; }
  .address-card .wordmark { right: 40px; top: 236px; font-size: 40px; }
</style>
</head>
<body>

<section class="band band--dark">
  <article class="card card--landscape front-landscape">
    <svg class="card-art" viewBox="0 0 540 330" aria-hidden="true"><polygon points="110,155 470,105 540,105 540,330 300,330" fill="var(--navy)"/></svg>
    <div class="wordmark">GROUT &amp; LEVEL</div>
  </article>

  <article class="card card--portrait back back-turned">
    <svg class="card-art" viewBox="0 0 330 540" aria-hidden="true">
      <rect width="330" height="540" fill="var(--white)"/>
      <polygon points="0,250 115,185 330,185 330,540 0,540" fill="var(--sky)"/>
      <rect x="0" y="38" width="42" height="24" fill="var(--red)"/>
      <rect x="288" y="38" width="42" height="24" fill="var(--red)"/>
    </svg>
    <div class="identity">
      <div class="company">GROUT &amp; LEVEL</div>
      <div class="licence">L : 204618c</div>
      <div class="person">Linh Tran</div>
      <div class="role">Project Manager</div>
    </div>
    <ul class="contacts">
      <li><svg viewBox="0 0 34 34" aria-hidden="true"><polygon points="10,1 24,1 33,10 33,24 24,33 10,33 1,24 1,10" fill="var(--red)"/><rect x="12" y="9" width="10" height="16" rx="2" fill="none" stroke="#fff" stroke-width="2"/></svg>0400 000 123</li>
      <li><svg viewBox="0 0 34 34" aria-hidden="true"><polygon points="10,1 24,1 33,10 33,24 24,33 10,33 1,24 1,10" fill="var(--red)"/><rect x="10" y="12" width="14" height="10" fill="#fff"/><polyline points="10,12 17,18 24,12" fill="none" stroke="var(--red)" stroke-width="1.5"/></svg>info@groutandlevel.com.au</li>
      <li><svg viewBox="0 0 34 34" aria-hidden="true"><polygon points="10,1 24,1 33,10 33,24 24,33 10,33 1,24 1,10" fill="var(--red)"/><circle cx="17" cy="17" r="7" fill="none" stroke="#fff" stroke-width="2"/><line x1="10" y1="17" x2="24" y2="17" stroke="#fff" stroke-width="2"/></svg>www.groutandlevel.com.au</li>
    </ul>
  </article>
</section>

<section class="band band--light">
  <article class="card card--portrait front-portrait">
    <svg class="card-art" viewBox="0 0 330 540" aria-hidden="true"><polygon points="140,470 140,90 330,0 330,230" fill="var(--navy)"/></svg>
    <div class="wordmark">GROUT &amp; LEVEL</div>
  </article>

  <article class="card card--portrait back back-upright">
    <svg class="card-art" viewBox="0 0 330 540" aria-hidden="true">
      <rect width="330" height="540" fill="var(--white)"/>
      <polygon points="0,250 115,185 330,185 330,540 0,540" fill="var(--sky)"/>
      <rect x="0" y="38" width="42" height="24" fill="var(--red)"/>
      <rect x="288" y="38" width="42" height="24" fill="var(--red)"/>
    </svg>
    <div class="identity">
      <div class="company">GROUT &amp; LEVEL</div>
      <div class="licence">L : 204618c</div>
      <div class="person">Linh Tran</div>
      <div class="role">Project Manager</div>
    </div>
    <ul class="contacts">
      <li><svg viewBox="0 0 34 34" aria-hidden="true"><polygon points="10,1 24,1 33,10 33,24 24,33 10,33 1,24 1,10" fill="var(--red)"/><rect x="12" y="9" width="10" height="16" rx="2" fill="none" stroke="#fff" stroke-width="2"/></svg>0400 000 123</li>
      <li><svg viewBox="0 0 34 34" aria-hidden="true"><polygon points="10,1 24,1 33,10 33,24 24,33 10,33 1,24 1,10" fill="var(--red)"/><rect x="10" y="12" width="14" height="10" fill="#fff"/><polyline points="10,12 17,18 24,12" fill="none" stroke="var(--red)" stroke-width="1.5"/></svg>info@groutandlevel.com.au</li>
      <li><svg viewBox="0 0 34 34" aria-hidden="true"><polygon points="10,1 24,1 33,10 33,24 24,33 10,33 1,24 1,10" fill="var(--red)"/><circle cx="17" cy="17" r="7" fill="none" stroke="#fff" stroke-width="2"/><line x1="10" y1="17" x2="24" y2="17" stroke="#fff" stroke-width="2"/></svg>www.groutandlevel.com.au</li>
    </ul>
  </article>
</section>

<section class="band band--blue">
  <article class="card card--wide address-card">
    <svg class="card-art" viewBox="0 0 620 378" aria-hidden="true"><polygon points="200,290 560,220 620,150 620,290 560,378 230,378" fill="var(--navy)"/></svg>
    <div class="details">
      <div class="company">GROUT &amp; LEVEL</div>
      <div>PO Box 48 Greenfield Park</div>
      <div>NSW 2176</div>
      <div><span class="label">M :</span> 0400 000 123</div>
    </div>
    <div class="wordmark">GROUT &amp; LEVEL</div>
  </article>
</section>

</body>
</html>
```